Create website for home automation - Control your lighting, fans, blinds etc remotely by smartphone

Plan for STOREVAN Website - Brightnest Dwellings
Company name: Brightnest Dwellings
Company Slogan: Calm Evenings Done Right
Clean, Modern, Easy to Navigate, easy to maintain - not a lot of coding. We need flash technology but displaying simply what we do.
What we provide:
We will be offering wireless switch which can be added to iOS/Android App via WiFi, allowing users to remotely turn on/off connected lights, fans, security cameras, appliances, irrigation, humidifier separately from anywhere at any time.
Control your home away from home. No more wandering of your mind on those lights or appliances which you might have left switched on. No need to drive back home to check and switch them off. Save that energy, money and time just with a click of your phone no matter how far you are from home.
Replace your home electrical switches with smart switches. They retrofit existing electrical switches and allow you to make the transformation as needed.
Easy to use and intuitive app allows you to control your lights and devices just at a click. Set any kind of ambiance suiting your occasion.
Set scenes in smartphone app to group and operate your devices just at a button click. Same device can be included in more than one scene.
Collections and Products
Light Switches
Wall Plugs
Fan Switch
Pendants etc special lighting types.
Light Dimmers
Blind Controllers
Home Page:
Home page needs to telling customers what we do and how we do it in a few words to grab people.
Logo
Phone
Email
Support – Download instructions per product
Client login
Wholesale login
Promotional video to be on home screen - this is a short 1.5 - 2 min illustration introduction video to who we are and what we do - this is yet to be created)
Social media link - Facebook
Pages:
FAQ
About Us
Support/Shipping/Returns policy
Support/Installation
Blog posts
Product pages:
Description
Price
Space for where a video will be featured - how each product works/installation.
Reviews
Our competition:
http://www.pvorn.com.au
https://lumalodgeguide.com.au/2018/04/05/best-smart-light-switches-and-plugs/
https://www.zentiqo.com
Attachments:
Logo
Product pics
Promotional video - if ready

```html
<!DOCTYPE html>
<html lang="en">
<head>
<meta charset="utf-8">
<title>Brightnest Dwellings – Home Automation</title>
<link rel="stylesheet" href="https://fonts.googleapis.com/css2?family=Montserrat:wght@400;500;600;700&family=Lato:ital,wght@0,400;1,400&display=swap">
<style>
:root{
  --navy:#12306b;
  --blue:#1a6fc0;
  --blue-dark:#1c3f8c;
  --ink:#222831;
  --text:#3b3f46;
  --muted:#6f7782;
  --pale:#f4f7fb;
  --footer:#3d4a60;
  --footer-line:#56637a;
  --white:#ffffff;
}
*{box-sizing:border-box;margin:0;padding:0}
html,body{width:1200px;height:2550px;overflow:hidden}
body{position:relative;background:var(--pale);font-family:"Montserrat",sans-serif;color:var(--text)}
.abs{position:absolute}

/* top bar */
.topbar{left:0;top:0;width:1200px;height:30px;background:var(--navy);color:var(--white);font-size:10px;font-weight:500}
.topbar .support{left:162px;top:0;height:30px;display:flex;align-items:center;gap:6px}
.topbar .socials{left:232px;top:7px;display:flex;gap:6px}
.topbar .socials span{width:16px;height:16px;border:1.5px solid var(--white);border-radius:50%}
.topbar .login{left:870px;top:0;height:30px;display:flex;align-items:center;gap:5px}
.topbar .wholesale{left:925px;top:0;width:114px;height:30px;background:var(--blue);display:flex;align-items:center;justify-content:center;gap:5px}

/* header */
.header{left:0;top:30px;width:1200px;height:67px;background:var(--white)}
.brand{left:162px;top:14px;display:flex;align-items:center;gap:10px}
.brand-mark{width:34px;height:34px;border:3px solid var(--blue-dark);border-radius:4px}
.brand-name{font-size:18px;font-weight:700;color:var(--blue-dark);line-height:1}
.brand-tag{font-size:8px;font-weight:500;color:var(--blue);letter-spacing:.6px;margin-top:3px}
.nav{right:161px;top:0;height:67px;display:flex;align-items:center;gap:36px;font-size:10.5px;font-weight:600;color:var(--ink)}

/* hero */
.hero{left:0;top:97px;width:1200px;height:560px}
.hero-photo{position:absolute;inset:0;background:
  linear-gradient(90deg,rgba(255,255,255,.78) 0%,rgba(255,255,255,.55) 45%,rgba(255,255,255,0) 62%),
  linear-gradient(160deg,#e9e3da 0%,#d8cdbf 30%,#c8d8ea 62%,#7fa9d8 78%,#c6d6e6 100%)}
.hero-curve{position:absolute;left:0;bottom:0}
.hero-copy{left:162px;top:174px;width:460px}
.hero-copy h1{font-size:23px;font-weight:700;color:var(--ink);letter-spacing:.3px}
.hero-copy .sub{margin-top:18px;font-size:14px;font-weight:500;color:var(--ink)}
.hero-copy p{margin-top:16px;font-size:13px;line-height:20px;color:var(--ink)}
.btn{display:inline-flex;align-items:center;justify-content:center;background:var(--blue);color:var(--white);font-size:10px;font-weight:600;border-radius:3px}
.hero-copy .btn{margin-top:26px;width:114px;height:35px}
.arrow{width:58px;height:58px;border-radius:50%;background:rgba(60,60,60,.75);display:flex;align-items:center;justify-content:center}
.scroll{left:588px;top:540px;width:22px;height:64px;background:var(--white);border-radius:11px;display:flex;align-items:center;justify-content:center}
.scroll span{transform:rotate(-90deg);font-size:9px;font-weight:600;color:var(--ink);letter-spacing:.6px}
.scroll-line{left:599px;top:604px;width:2px;height:84px;background:#555}

/* section heads */
.section-head{left:0;width:1200px;text-align:center}
.section-head svg{display:block;margin:0 auto}
.section-head .eyebrow{margin-top:2px;font-size:13px;font-weight:700;color:var(--ink)}
.section-head h2{margin-top:2px;font-size:30px;font-weight:700;color:var(--blue-dark)}
.intro{left:300px;top:832px;width:600px;text-align:center;font-size:11px;line-height:20px;color:var(--ink)}

/* products */
.product{width:150px;text-align:center}
.product h3{font-size:11px;font-weight:700;color:var(--blue)}
.product p{margin-top:6px;font-size:11px;line-height:17px;color:var(--ink)}

/* what we do */
.wwd-copy{left:162px;top:1352px;width:430px}
.wwd-copy h3{font-size:16px;font-weight:600;color:var(--ink)}
.wwd-copy p{margin-top:14px;font-size:10.5px;line-height:19.4px;color:var(--ink)}
.wwd-copy .btn{margin-top:24px;width:128px;height:33px}
.video{left:612px;top:1358px;width:427px;height:284px;background:linear-gradient(135deg,#8e8f91,#a3a4a6 40%,#7d7f82);border:1px solid #ccc}
.video .play{position:absolute;left:176px;top:105px;width:76px;height:76px;border-radius:50%;background:var(--white);display:flex;align-items:center;justify-content:center;box-shadow:0 2px 8px rgba(0,0,0,.25)}
.video-caption{left:612px;top:1668px;font-size:10px;font-weight:600;color:var(--ink)}

/* testimonials */
.testimonials{left:0;top:1737px;width:1200px;height:524px;background:linear-gradient(180deg,#e6e4e2,#d9dde4 45%,#e3ddd6 100%)}
.testimonial-card{left:162px;top:1924px;width:877px;height:258px;background:var(--white);box-shadow:0 2px 10px rgba(0,0,0,.08)}
.quote-mark{position:absolute;font-family:Georgia,serif;font-size:110px;line-height:1;color:#d3d6db}
.testimonial-card blockquote{position:absolute;left:150px;top:42px;width:580px;text-align:center;font-family:"Lato",sans-serif;font-style:italic;font-size:17px;line-height:29px;color:var(--ink)}
.testimonial-card .who{position:absolute;left:0;width:877px;top:200px;text-align:center;font-size:15px;color:var(--ink)}
.testimonial-card .who span{color:var(--blue)}

/* footer */
.footer{left:0;top:2261px;width:1200px;height:289px;background:var(--footer);color:var(--white)}
.footer-nav{left:0;top:28px;width:1200px;display:flex;justify-content:center;font-size:10px;font-weight:600}
.footer-nav span{padding:0 18px;border-left:1px solid var(--footer-line)}
.footer-nav span:first-child{border-left:none}
.footer-rule{left:162px;top:58px;width:877px;height:1px;background:var(--footer-line)}
.footer h4{display:flex;align-items:center;gap:12px;font-size:14px;font-weight:500}
.footer h4::before{content:"";width:30px;height:1px;background:var(--white)}
.about-col{left:162px;top:78px;width:340px}
.about-col p{margin-top:10px;font-size:10px;line-height:17px;color:#d8dde6}
.about-col a{display:inline-block;margin-top:10px;font-size:10px;font-weight:600;color:var(--white);text-decoration:underline}
.contact-col{left:588px;top:78px;width:451px}
.contact-row{margin-top:14px;display:flex;align-items:center;gap:8px;font-size:10px;color:#d8dde6}
.contact-socials{position:absolute;right:0;top:24px;display:flex;gap:4px}
.contact-socials span{width:26px;height:26px;border:1.5px solid var(--white);border-radius:50%}
.news-col{left:588px;top:160px;width:451px}
.news-col p{margin-top:10px;font-size:10px;color:#d8dde6}
.news-form{margin-top:10px;display:flex;height:33px}
.news-form .field{flex:1;background:var(--white);color:var(--ink);font-size:10px;font-weight:500;display:flex;align-items:center;gap:6px;padding-left:12px;border-right:1px solid #ccc}
.news-form .send{width:82px;background:var(--blue);display:flex;align-items:center;justify-content:center;font-size:11px;font-weight:700}
.copyright{left:162px;top:243px;font-size:9.5px;color:#d8dde6}
.copyright b{color:var(--white);font-weight:600}
</style>
</head>
<body>

<div class="abs topbar">
  <div class="abs support">
    <svg width="12" height="12" viewBox="0 0 12 12"><circle cx="6" cy="6" r="4.5" fill="none" stroke="#fff" stroke-width="1.3"/><circle cx="6" cy="6" r="1.8" fill="none" stroke="#fff" stroke-width="1.3"/></svg>
    Support
  </div>
  <div class="abs socials"><span></span><span></span><span></span></div>
  <div class="abs login">
    <svg width="10" height="12" viewBox="0 0 10 12"><rect x="1" y="5" width="8" height="6" rx="1" fill="none" stroke="#fff" stroke-width="1.2"/><path d="M3 5V3.5a2 2 0 0 1 4 0V5" fill="none" stroke="#fff" stroke-width="1.2"/></svg>
    Login
  </div>
  <div class="abs wholesale">
    <svg width="12" height="12" viewBox="0 0 12 12"><circle cx="6" cy="6" r="4.5" fill="none" stroke="#fff" stroke-width="1.3"/><path d="M1.5 6h9M6 1.5c2 2.5 2 6.5 0 9M6 1.5c-2 2.5-2 6.5 0 9" fill="none" stroke="#fff" stroke-width="1"/></svg>
    Wholesale Login
  </div>
</div>

<header class="abs header">
  <div class="abs brand">
    <div class="brand-mark"></div>
    <div>
      <div class="brand-name">BRIGHTNEST DWELLINGS</div>
      <div class="brand-tag">Calm Evenings Done Right</div>
    </div>
  </div>
  <nav class="abs nav">
    <span>HOME</span><span>ABOUT US</span><span>PRODUCT</span><span>SUPPORT ⌄</span><span>BLOG</span><span>CONTACT US</span>
  </nav>
</header>

<section class="abs hero">
  <div class="hero-photo" role="img" aria-label="Bright living room interior with a hand holding a smartphone showing home control app icons"></div>
  <svg class="hero-curve" width="1200" height="120" viewBox="0 0 1200 120"><path d="M0 0 Q600 140 1200 0 V120 H0 Z" fill="#f4f7fb"/></svg>
  <div class="abs hero-copy">
    <h1>BEST HOME AUTOMATION</h1>
    <div class="sub">LOREM IPSUM DOLOR SIT AMET</div>
    <p>Donec imperdiet enim varius est ultrices sollicitudin. Phasellus erat libero, ultrices eget fringilla efficitur, efficitur vitae felis. Aliquam quis aliquam nunc. Fusce eget nunc eget turpis mattis hendrerit.</p>
    <span class="btn">LEARN MORE</span>
  </div>
  <div class="abs arrow" style="left:48px;top:228px"><svg width="18" height="14" viewBox="0 0 18 14"><path d="M17 7H2M7 1 1 7l6 6" fill="none" stroke="#fff" stroke-width="2"/></svg></div>
  <div class="abs arrow" style="left:1092px;top:228px"><svg width="18" height="14" viewBox="0 0 18 14"><path d="M1 7h15M11 1l6 6-6 6" fill="none" stroke="#fff" stroke-width="2"/></svg></div>
</section>
<div class="abs scroll"><span>SCROLL</span></div>
<div class="abs scroll-line"></div>

<div class="abs section-head" style="top:738px">
  <svg width="34" height="20" viewBox="0 0 34 20"><path d="M3 10a20 20 0 0 1 28 0M8 15a13 13 0 0 1 18 0M13 19a6 6 0 0 1 8 0" fill="none" stroke="#1a6fc0" stroke-width="3"/></svg>
  <div class="eyebrow">ABOUT US</div>
  <h2>WHO WE ARE</h2>
</div>
<p class="abs intro">Lorem ipsum dolor sit amet, consectetur adipiscing elit. Donec imperdiet enim varius est ultrices sollicitudin. Phasellus erat libero, ultrices eget fringilla efficitur, efficitur vitae felis. Aliquam quis aliquam nunc.</p>

<svg class="abs" style="left:0;top:900px" width="1200" height="220" viewBox="0 0 1200 220">
  <g fill="none" stroke="#9aa3ad" stroke-width="1.2" stroke-dasharray="2 3">
    <path d="M266 57 C320 57 360 90 374 120"/>
    <path d="M374 120 C390 80 440 57 482 57"/>
    <path d="M566 57 C620 57 660 90 675 120"/>
    <path d="M675 120 C690 80 740 57 781 57"/>
    <path d="M865 57 C920 57 960 90 974 120"/>
  </g>
  <g fill="#fff" stroke="#1a6fc0">
    <circle cx="224" cy="57" r="41" stroke-width="1" stroke="#b9cfe8"/><circle cx="224" cy="57" r="34" stroke-width="2"/>
    <circle cx="374" cy="162" r="41" stroke-width="1" stroke="#b9cfe8"/><circle cx="374" cy="162" r="34" stroke-width="2"/>
    <circle cx="524" cy="57" r="41" stroke-width="1" stroke="#b9cfe8"/><circle cx="524" cy="57" r="34" stroke-width="2"/>
    <circle cx="675" cy="162" r="41" stroke-width="1" stroke="#b9cfe8"/><circle cx="675" cy="162" r="34" stroke-width="2"/>
    <circle cx="823" cy="57" r="41" stroke-width="1" stroke="#b9cfe8"/><circle cx="823" cy="57" r="34" stroke-width="2"/>
    <circle cx="974" cy="162" r="41" stroke-width="1" stroke="#b9cfe8"/><circle cx="974" cy="162" r="34" stroke-width="2"/>
  </g>
  <g fill="none" stroke="#1c3f8c" stroke-width="1.8">
    <rect x="210" y="42" width="28" height="30" rx="2"/><rect x="216" y="50" width="6" height="14"/><rect x="226" y="50" width="6" height="14"/>
    <rect x="360" y="148" width="28" height="28" rx="4"/><circle cx="369" cy="162" r="2"/><circle cx="379" cy="162" r="2"/>
    <rect x="512" y="40" width="24" height="34" rx="2"/><rect x="518" y="48" width="12" height="18"/>
    <path d="M675 140v12M664 172h22l-4-14h-14z"/><path d="M675 175v3"/>
    <rect x="809" y="42" width="28" height="30" rx="2"/><path d="M815 64V50M823 64V50M831 64V50"/><circle cx="815" cy="56" r="2"/><circle cx="823" cy="60" r="2"/><circle cx="831" cy="53" r="2"/>
    <rect x="959" y="148" width="30" height="28" rx="2"/><path d="M963 154h22M963 160h22M963 166h22M963 172h22"/>
  </g>
</svg>
<div class="abs product" style="left:149px;top:1020px"><h3>LIGHT SWITCHES</h3><p>Suspendisse auctor interdum tellus ut sodales.</p></div>
<div class="abs product" style="left:299px;top:1125px"><h3>WALL PLUGS</h3><p>Suspendisse auctor interdum tellus ut sodales.</p></div>
<div class="abs product" style="left:449px;top:1020px"><h3>FAN SWITCH</h3><p>Suspendisse auctor interdum tellus ut sodales.</p></div>
<div class="abs product" style="left:600px;top:1125px"><h3>PENDANTS</h3><p>Suspendisse auctor interdum tellus ut sodales.</p></div>
<div class="abs product" style="left:748px;top:1020px"><h3>LIGHT DIMMERS</h3><p>Suspendisse auctor interdum tellus ut sodales.</p></div>
<div class="abs product" style="left:899px;top:1125px"><h3>BLIND CONTROLLERS</h3><p>Suspendisse auctor interdum tellus ut sodales.</p></div>

<div class="abs section-head" style="top:1240px">
  <svg width="34" height="20" viewBox="0 0 34 20"><path d="M3 10a20 20 0 0 1 28 0M8 15a13 13 0 0 1 18 0M13 19a6 6 0 0 1 8 0" fill="none" stroke="#1a6fc0" stroke-width="3"/></svg>
  <div class="eyebrow">HOW IT WORKS</div>
  <h2>WHAT WE DO</h2>
</div>
<div class="abs wwd-copy">
  <h3>Suspendisse auctor interdum tellus ut sodales</h3>
  <p>Lorem ipsum dolor sit amet, consectetur adipiscing elit. Donec imperdiet enim varius est ultrices sollicitudin. Phasellus erat libero, ultrices eget fringilla efficitur, efficitur vitae felis. Aliquam quis aliquam nunc. Fusce eget nunc eget turpis mattis hendrerit id quis arcu. Ut sed risus sed dui tincidunt imperdiet non non nibh. Donec sed elit ac mauris condimentum egestas a in mauris. Nulla facilisi. Morbi enim metus, condimentum sed tortor ac, rhoncus ornare tellus. Nam mollis risus a pretium iaculis. Praesent gravida nulla ac pellentesque feugiat. Suspendisse dignissim varius lacus vitae porta. Fusce feugiat leo metus, sit amet ullamcorper nisl interdum quis. Pellentesque malesuada felis pharetra turpis egestas blandit. Suspendisse potenti.</p>
  <span class="btn">LEARN MORE</span>
</div>
<div class="abs video" role="img" aria-label="Video still: illustrated house surrounded by security devices such as alarm, intercom, camera and sensors">
  <div class="play"><svg width="26" height="30" viewBox="0 0 26 30"><path d="M3 2 24 15 3 28z" fill="#1a6fc0"/></svg></div>
</div>
<div class="abs video-caption">HOW IT WORKS? WATCH VIDEO</div>
<svg class="abs" style="left:795px;top:1650px" width="62" height="40" viewBox="0 0 62 40"><path d="M4 32 C24 38 44 30 54 8" fill="none" stroke="#222831" stroke-width="2.5"/><path d="M46 10 55 5 57 16" fill="none" stroke="#222831" stroke-width="2.5"/></svg>

<section class="abs testimonials" role="img" aria-label="Softly blurred living room background"></section>
<div class="abs section-head" style="top:1800px">
  <svg width="34" height="20" viewBox="0 0 34 20"><path d="M3 10a20 20 0 0 1 28 0M8 15a13 13 0 0 1 18 0M13 19a6 6 0 0 1 8 0" fill="none" stroke="#1a6fc0" stroke-width="3"/></svg>
  <div class="eyebrow">TESTIMONIALS</div>
  <h2>WHAT DO OUR CUSTOMERS THINK OF US</h2>
</div>
<div class="abs testimonial-card">
  <span class="quote-mark" style="left:62px;top:14px">“</span>
  <span class="quote-mark" style="left:762px;top:166px">”</span>
  <blockquote>Lorem ipsum dolor sit amet, consectetur adipiscing elit. Donec imperdiet enim varius est ultrices sollicitudin. Phasellus erat libero, ultrices eget fringilla efficitur, efficitur vitae felis. Aliquam quis aliquam nunc. Fusce eget nunc eget turpis mattis hendrerit id quis arcu.</blockquote>
  <div class="who"><span>CUSTOMER NAME</span>, LOCATION</div>
</div>

<footer class="abs footer">
  <div class="abs footer-nav"><span>HOME</span><span>ABOUT US</span><span>PRODUCT</span><span>SUPPORT</span><span>BLOG</span><span>CONTACT US</span></div>
  <div class="abs footer-rule"></div>
  <div class="abs about-col">
    <h4>About Brightnest Dwellings</h4>
    <p>Lorem ipsum dolor sit amet, consectetur adipiscing elit. Donec imperdiet enim varius est ultrices sollicitudin. Phasellus erat libero, ultrices eget fringilla efficitur, efficitur vitae felis.</p>
    <a>Read More</a>
  </div>
  <div class="abs contact-col">
    <h4>Contact Us</h4>
    <div class="contact-row">
      <svg width="11" height="11" viewBox="0 0 11 11"><path d="M2 1l2 2-1 2a6 6 0 0 0 3 3l2-1 2 2-1.5 1.5C5 10 1 6 .5 2.5z" fill="none" stroke="#d8dde6" stroke-width="1"/></svg>
      (000) 123 456 7890
      <svg style="margin-left:18px" width="12" height="9" viewBox="0 0 12 9"><rect x=".5" y=".5" width="11" height="8" fill="none" stroke="#d8dde6"/><path d="M.5.5 6 5l5.5-4.5" fill="none" stroke="#d8dde6"/></svg>
      info@brightnestdwellings.com
    </div>
    <div class="contact-socials"><span></span><span></span><span></span></div>
  </div>
  <div class="abs news-col">
    <h4>Newsletter</h4>
    <p>Sign up for our mailing list to get latest updates and offers</p>
    <div class="news-form">
      <div class="field"><svg width="9" height="10" viewBox="0 0 9 10"><circle cx="4.5" cy="3" r="2.5" fill="#555"/><path d="M0 10a4.5 4.5 0 0 1 9 0z" fill="#555"/></svg>Name</div>
      <div class="field"><svg width="11" height="8" viewBox="0 0 11 8"><rect width="11" height="8" fill="#555"/><path d="M0 0l5.5 4L11 0" fill="none" stroke="#fff"/></svg>Email Address</div>
      <div class="send">SEND</div>
    </div>
  </div>
  <div class="abs copyright">Copyright © 2018 <b>Brightnest Dwellings</b>. All Rights Reserved.</div>
</footer>

</body>
</html>
```